Post it Note design

POST-IT NOTE DESIGN (CONTENT)
Size recommended: 4x6 for handwriting space.
Header (Bold):
Lighting Issue Detected on Your Property
Sub-header:
During our routine night inspection, we noted the following item(s):
Checkbox List:
⬜ Building Lights Out
⬜ Pole Lights Out
⬜ Sign Not Illuminated
⬜ Other ________________________
Action Line:
We can provide a quote or dispatch service right away.
Area for notes
Contact Block (Bold & Centered):
Brightwell Fixture Care Inc.
Service@BrightwellFixtureCare.com
www.BrightwellFixtureCare.com
877-514-6082
Industry/Entity Type
Electrical lighting
Colors
Designer to choose colors to be used in the design.
Look and feel
Each slider illustrates characteristics of the customer's brand and the style your logo design should communicate.

```html
<!DOCTYPE html>
<html lang="en">
<head>
<meta charset="UTF-8">
<title>Lighting Issue Detected – Brightwell Fixture Care Inc.</title>
<link rel="stylesheet" href="https://fonts.googleapis.com/css2?family=Anton&family=Rubik:wght@400;500;700;800&display=swap">
<style>
  :root {
    --page-bg: #b4b4b4;
    --paper: #f4f4f5;
    --navy: #1b2a86;
    --royal: #2a44b8;
    --red: #df0a10;
    --white: #ffffff;
    --muted: #c9c9cc;
  }
  * { margin: 0; padding: 0; box-sizing: border-box; }
  html, body { width: 1200px; height: 1200px; overflow: hidden; }
  body {
    background: var(--page-bg);
    font-family: "Rubik", Arial, sans-serif;
    position: relative;
  }
  .note {
    position: absolute;
    left: 220px; top: 30px;
    width: 760px; height: 1140px;
    background: var(--paper);
    overflow: hidden;
    box-shadow: 0 10px 30px rgba(0,0,0,.18);
  }
  .header-band {
    position: absolute; left: 0; top: 0;
    width: 760px; height: 450px;
  }
  .header-photo {
    position: absolute; right: 0; top: 0;
    width: 420px; height: 405px;
    background: radial-gradient(circle at 60% 35%, #6f86e0 0%, #3552c6 45%, #2239a8 100%);
    clip-path: polygon(0 0, 100% 0, 100% 350px, 0 405px);
    opacity: .9;
  }
  .headline {
    position: absolute; left: 48px; top: 80px;
    font-family: "Anton", Impact, sans-serif;
    font-size: 70px; line-height: 1.02;
    color: var(--white);
    text-transform: uppercase;
    letter-spacing: .5px;
  }
  .subhead {
    position: absolute; left: 48px; top: 308px;
    font-size: 24px; line-height: 1.3;
    color: var(--white);
  }
  .checklist {
    position: absolute; left: 70px; top: 480px;
    list-style: none;
  }
  .checklist li {
    display: flex; align-items: center;
    height: 62px;
    font-size: 32px; color: var(--navy);
  }
  .checkbox {
    width: 36px; height: 36px;
    border: 3px solid var(--navy);
    margin-right: 30px;
    flex: none;
  }
  .write-line {
    position: absolute; left: 300px; top: 710px;
    width: 410px; height: 2px;
    background: var(--navy);
  }
  .brand-name {
    position: absolute; left: 0; top: 752px; width: 760px;
    text-align: center;
    font-size: 34px; font-weight: 800;
    color: var(--red);
  }
  .notes-box {
    position: absolute; left: 120px; top: 860px;
    width: 600px; height: 170px;
    border: 3px dotted var(--navy);
    border-radius: 18px;
  }
  .notes-label {
    position: absolute; left: 10px; bottom: 14px;
    writing-mode: vertical-rl;
    transform: rotate(180deg);
    font-size: 34px; letter-spacing: 2px;
    color: var(--muted);
  }
  .action-banner {
    position: absolute; left: 120px; top: 812px;
    width: 480px; height: 78px;
    background: var(--red);
    border-radius: 14px;
    color: var(--white);
    font-weight: 700; font-size: 22px; line-height: 1.25;
    display: flex; align-items: center; justify-content: center;
    text-align: center;
  }
  .truck-photo {
    position: absolute; right: 0; top: 862px;
    width: 200px; height: 130px;
    background: linear-gradient(160deg, #fdfdfd 0%, #e3e4e8 55%, #9a9ca4 100%);
  }
  .contact-band {
    position: absolute; left: 0; bottom: 0;
    width: 760px; height: 96px;
  }
  .phone {
    position: absolute; left: 24px; bottom: 22px;
    display: flex; align-items: center; gap: 10px;
    color: var(--white);
    font-size: 42px; font-weight: 500;
  }
  .web-contacts {
    position: absolute; right: 18px; bottom: 18px;
    color: var(--white);
    font-size: 16px; line-height: 1.75;
    list-style: none;
    white-space: nowrap;
  }
  .web-contacts li { display: flex; align-items: center; gap: 8px; }
</style>
</head>
<body>
  <article class="note">
    <svg class="header-band" viewBox="0 0 760 450" aria-hidden="true">
      <defs>
        <linearGradient id="headerFill" x1="0" y1="0" x2="0" y2="1">
          <stop offset="0" stop-color="#2a44b8"/>
          <stop offset="1" stop-color="#1b2a86"/>
        </linearGradient>
      </defs>
      <polygon points="0,0 760,0 760,350 0,450" fill="url(#headerFill)"/>
    </svg>
    <div class="header-photo" role="img" aria-label="Photo of a technician servicing pole-mounted light fixtures at dusk, tinted blue"></div>

    <h1 class="headline">Lighting Issue<br>Detected on<br>Your Property</h1>
    <p class="subhead">During our routine night inspection,<br>we noted the following item(s):</p>

    <ul class="checklist">
      <li><span class="checkbox"></span>Building Lights Out</li>
      <li><span class="checkbox"></span>Pole Lights Out</li>
      <li><span class="checkbox"></span>Sign Not Illuminated</li>
      <li><span class="checkbox"></span>Other</li>
    </ul>
    <div class="write-line"></div>

    <div class="brand-name">Brightwell Fixture Care Inc.</div>

    <div class="notes-box"><span class="notes-label">NOTES</span></div>
    <div class="action-banner">We can provide a quote or dispatch<br>service right away.</div>
    <div class="truck-photo" role="img" aria-label="Photo of a white bucket service truck with traffic cones"></div>

    <svg class="contact-band" viewBox="0 0 760 96" aria-hidden="true">
      <rect x="0" y="0" width="760" height="96" fill="#1b2a86"/>
      <polygon points="0,0 392,0 410,96 0,96" fill="#df0a10"/>
    </svg>
    <div class="phone">
      <svg width="28" height="28" viewBox="0 0 24 24" aria-hidden="true">
        <path fill="#fff" d="M6.6 10.8a15.1 15.1 0 0 0 6.6 6.6l2.2-2.2c.3-.3.7-.4 1-.2 1.1.4 2.3.6 3.6.6.6 0 1 .4 1 1V20c0 .6-.4 1-1 1A17 17 0 0 1 3 4c0-.6.4-1 1-1h3.5c.6 0 1 .4 1 1 0 1.3.2 2.5.6 3.6.1.3 0 .7-.2 1z"/>
      </svg>
      877-514-6082
    </div>
    <ul class="web-contacts">
      <li>
        <svg width="16" height="12" viewBox="0 0 16 12" aria-hidden="true"><rect x="0.5" y="0.5" width="15" height="11" fill="#fff"/><path d="M1 1l7 5 7-5" stroke="#1b2a86" stroke-width="1.4" fill="none"/></svg>
        Service@BrightwellFixtureCare.com
      </li>
      <li>
        <svg width="16" height="16" viewBox="0 0 16 16" aria-hidden="true"><circle cx="8" cy="8" r="7" fill="none" stroke="#fff" stroke-width="1.4"/><ellipse cx="8" cy="8" rx="3" ry="7" fill="none" stroke="#fff" stroke-width="1.2"/><path d="M1 8h14" stroke="#fff" stroke-width="1.2"/></svg>
        www.BrightwellFixtureCare.com
      </li>
    </ul>
  </article>
</body>
</html>
```